Bao Lotus Menu Design Project

This project is pretty straight forward. You will be given 3 files which include the following:
1. Our proposed menu
2. Our Company logo
3. A sample menu on what we are looking for design wise

Your job is to create a visually pleasing menu that is simple, clean and fresh. Please refer to our home website for additional information. (www.baolotus-example.com) Must be in eps or equivalent format.

Target Market(s)

20s to 40s

Industry/Entity Type

It Company

Requirements
Must have
• Company log
Must be in EPS format

```html
<!DOCTYPE html>
<html lang="en">
<head>
<meta charset="utf-8">
<title>Bao Lotus Menu</title>
<link href="https://fonts.googleapis.com/css2?family=Open+Sans:wght@700;800&family=PT+Sans+Narrow:wght@400;700&display=swap" rel="stylesheet">
<style>
  :root {
    --page-bg: #3a3a3a;
    --menu-bg: #221d1f;
    --heading: #f6efe2;
    --item: #f3e9d4;
    --desc: #e4dccd;
    --brand-red: #e3101b;
    --photo-warm: #5a3b25;
    --photo-deep: #2a1c16;
  }
  * { margin: 0; padding: 0; box-sizing: border-box; }
  html, body { width: 1200px; height: 900px; overflow: hidden; }
  body { background: var(--page-bg); position: relative; font-family: "PT Sans Narrow", "Arial Narrow", sans-serif; }

  .menu {
    position: absolute; left: 280px; top: 37px;
    width: 640px; height: 826px;
    background: var(--menu-bg);
    overflow: hidden;
  }
  .interior-photo {
    position: absolute; left: 180px; top: 400px; width: 460px; height: 382px;
    background:
      radial-gradient(ellipse at 55% 70%, rgba(120,80,50,.75), rgba(60,40,28,.4) 45%, transparent 75%),
      linear-gradient(180deg, var(--menu-bg) 0%, var(--photo-deep) 35%, var(--photo-warm) 80%, var(--photo-deep) 100%);
    opacity: .9;
  }
  .columns {
    position: absolute; left: 40px; top: 48px; right: 40px;
    display: flex; justify-content: space-between;
  }
  .column { width: 176px; text-align: center; }
  .section-title {
    font-family: "Open Sans", Arial, sans-serif; font-weight: 800;
    font-size: 15px; color: var(--heading); letter-spacing: .2px;
    margin-bottom: 5px;
  }
  .section-title.spaced { margin-top: 10px; }
  .section-note { font-size: 10px; color: var(--desc); margin: -2px 0 8px; }
  .dish { margin-bottom: 8px; }
  .dish-name { font-weight: 700; font-size: 11.5px; color: var(--item); text-transform: uppercase; line-height: 1.15; }
  .dish-price { font-weight: 700; font-size: 11.5px; color: var(--item); line-height: 1.2; }
  .dish-desc { font-size: 9.6px; color: var(--desc); line-height: 1.35; }

  .brand-name {
    position: absolute; left: 478px; top: 672px; width: 120px;
    font-family: "Open Sans", Arial, sans-serif; font-weight: 800;
    font-size: 34px; line-height: 1; color: var(--brand-red);
    text-transform: uppercase; text-align: center;
  }
  .brand-band {
    position: absolute; left: 0; bottom: 0; width: 100%; height: 44px;
    background: var(--brand-red);
  }
</style>
</head>
<body>
<main class="menu">
  <div class="interior-photo" role="img" aria-label="Dimly lit restaurant interior with booths and tables"></div>

  <div class="columns">
    <section class="column">
      <h2 class="section-title">DIM SUM</h2>
      <div class="dish"><p class="dish-name">Pan-Fried Potstickers</p><p class="dish-price">- 6.50</p><p class="dish-desc">Five pan-Fried potstickers with chicken or pork. Served with apricot dipping sauce.</p></div>
      <div class="dish"><p class="dish-name">Steamed Dumplings</p><p class="dish-price">- 6.50</p><p class="dish-desc">Five steamed dumplings with chicken, or vegetables. Served with apricot dipping sauce.</p></div>
      <div class="dish"><p class="dish-name">Szechuan Dumplings</p><p class="dish-price">- 6.25</p><p class="dish-desc">Five chicken dumplings tossed in a spicy cilantro sauce.</p></div>
      <div class="dish"><p class="dish-name">Spring Rolls</p><p class="dish-price">- 4.50</p><p class="dish-desc">Two chicken or vegetable spring rolls. Served with apricot dipping sauce.</p></div>
      <div class="dish"><p class="dish-name">Wonton Stars</p><p class="dish-price">- 7.25</p><p class="dish-desc">Five crispy wonton skins filled with real crab and seasoned cream cheese. Served with sweet and sour dipping sauce.</p></div>
      <div class="dish"><p class="dish-name">Bao</p><p class="dish-price">- 5.95</p><p class="dish-desc">Three fluffy steamed chinese buns filled with barbeque pork.</p></div>
      <div class="dish"><p class="dish-name">Shrimp Toast</p><p class="dish-price">- 5.95</p><p class="dish-desc">Four pieces of fried toast with shrimp, onions, bamboo shoots, and water chestnuts. Served with apricot dipping sauce.</p></div>
      <div class="dish"><p class="dish-name">Shu Mai</p><p class="dish-price">- 5.95</p><p class="dish-desc">Six steamed open-Face dumplings with pork, shrimp, and mushrooms.</p></div>
      <div class="dish"><p class="dish-name">Gift Wrapped Chicken</p><p class="dish-price">- 5.95</p><p class="dish-desc">Six chicken breast tenders marinated in soy sauce, sesame oil, and cilantro.</p></div>
      <div class="dish"><p class="dish-name">Assorted Pleasures</p><p class="dish-price">- 8.95</p><p class="dish-desc">Two chicken potstickers, two fried chicken wontons, two gift wrapped chicken, and one vegetable spring roll.</p></div>
    </section>

    <section class="column">
      <h2 class="section-title">STARTERS</h2>
      <div class="dish"><p class="dish-name">Edamame</p><p class="dish-price">- 4.00</p><p class="dish-desc">Steamed Soybean Pods.</p></div>
      <div class="dish"><p class="dish-name">Lightly Battered Calamari Strips</p><p class="dish-price">- 5.95</p><p class="dish-desc">Six calamari strips, lightly battered with a garlic ginger aioli.</p></div>
      <div class="dish"><p class="dish-name">4 C's Bao Lotus Crab Cake's</p><p class="dish-price">- 11.95</p><p class="dish-desc">Jumbo lump Maryland crab meat with seasoned with our Bao Lotus spice blend. Topped with a kick of spicy aioli.</p></div>

      <h2 class="section-title spaced">LUNCH / DINNER</h2>
      <div class="dish"><p class="dish-name">Dim Sum and Then Sum</p><p class="dish-price">- 14.95 / 18.95</p><p class="dish-desc">Choose three / four half orders: Potstickers,steamed dumplings, szechwan dumplings,spring roll, shrimp toast, chinese chicken salad, hot &amp; sour soup, wonton soup, or mushu, For Shrimp fried rice, beef fried rice, or mushu shrimp, add $1.00.</p></div>

      <h2 class="section-title spaced">SOUP</h2>
      <div class="dish"><p class="dish-name">SM.&nbsp;&nbsp;&nbsp;LG.</p><p class="dish-name">Wonton Soup</p><p class="dish-price">- 4.95&nbsp;&nbsp;7.50</p><p class="dish-desc">Chicken or pork wonton dumplings with spinach and scallions in chicken broth.</p></div>
      <div class="dish"><p class="dish-name">Miso Soup</p><p class="dish-price">- 4.95&nbsp;&nbsp;7.50</p><p class="dish-desc">Miso Based Soup with tofu and scallions</p></div>
      <div class="dish"><p class="dish-name">Hot and Sour Soup</p><p class="dish-price">- 4.95&nbsp;&nbsp;7.50</p><p class="dish-desc">Shredded pork, scallions, carrots, egg, and soft tofu.</p></div>
      <div class="dish"><p class="dish-name">Velvet Corn Soup</p><p class="dish-price">- 7.25</p><p class="dish-desc">Cellophane noodles, chicken, sweet corn, green peas, and egg. No modifications</p></div>
    </section>

    <section class="column">
      <h2 class="section-title">SALADS</h2>
      <p class="section-note">Can replace Chicken with Tofu for $1.50</p>
      <div class="dish"><p class="dish-name">Chinese Chicken Salad</p><p class="dish-price">- 10.50</p><p class="dish-desc">Shredded lettuce, chicken breast, breast and vegetables in a spicy browncrunchies, and white crunchies with tart red ginger dressing</p></div>
      <div class="dish"><p class="dish-name">Main Mein Salad</p><p class="dish-price">- 9.95</p><p class="dish-desc">Cold lo mein noodles with chicken breast, red cabbage, carrots, peanut dressing.</p></div>
      <div class="dish"><p class="dish-name">Sesame Chicken Salad</p><p class="dish-price">- 9.95</p><p class="dish-desc">Shredded lettuce, chicken breast, red cabbage, carrots, browncrunchies, fresh oranges, scallions, and sesame dressing.</p></div>
    </section>
  </div>

  <p class="brand-name">Bao Lotus</p>
  <div class="brand-band"></div>
</main>
</body>
</html>
```